Brightwell Rx Pass reinvent our website.

Our Website is outdated and needs an overhaul, in every aspect. We assist individuals that have little or no prescription coverage and allow them to receive a discount ranging from 33% up to 78% for free. In the beginning we utilized pharmacies to spread the word, but times have a changed. We are looking for a modern and clean site. We are open to anything, image, logo etc.

Target Market(s)

Anyone regardless of residency, age or income. This program is designed to assist those that have NO prescription coverage or for those whose particular prescription may not be covered by insurance.

Industry/Entity Type

Pharmaceutical

Coding

Coded - Design and coding required

Number of Pages Required

4 page

Requirements
Must have
• -The two MUST haves are the pharmacy locators & drug pricing. If you can combine the 2, even better.
• -a ongoing counter/tally on the 1stpage reflecting the amount of money we are saving customers. http://plumtreemarket.example/item/animated-counters-v-20-edge-animate-collection/full_screen_preview/52970314
• -on a smart phone the ability to view the information that is needed to get the actual discount for the medication.
Nice to have
• animated tutorial showing how to use the card
• health blog

```html
<!DOCTYPE html>
<html lang="en">
<head>
<meta charset="utf-8">
<title>Brightwell Rx Pass</title>
<link href="https://fonts.googleapis.com/css2?family=Open+Sans:wght@400;600;700&family=Roboto+Condensed:wght@400;700&family=Montserrat:wght@400;600;700&family=Lora:ital@1&display=swap" rel="stylesheet">
<style>
:root{
  --blue:#1b5fa8;
  --blue-dark:#124a86;
  --blue-light:#2f8be0;
  --red:#f2322a;
  --dark:#3d3d3d;
  --darker:#2b2b2b;
  --text:#333;
  --muted:#777;
  --white:#fff;
  --pale:#f1f3f5;
}
*{margin:0;padding:0;box-sizing:border-box}
html,body{width:1200px;height:4017px;overflow:hidden}
body{font-family:"Open Sans",sans-serif;color:var(--text);background:var(--white)}
.page{position:relative;width:1200px;height:4017px;overflow:hidden}
.abs{position:absolute}
.backdrop{position:absolute;left:0;top:0}

/* top bar & header */
.topbar{left:0;top:0;width:1200px;height:27px;background:var(--darker);color:#ddd;font-size:10px;line-height:27px;padding-left:133px}
.topbar span{margin-right:22px}
.header{left:0;top:27px;width:1200px;height:104px;background:linear-gradient(#f4f7fa,#e6ecf2)}
.brand{left:125px;top:66px;display:flex;align-items:center;gap:8px;font-family:"Montserrat",sans-serif;font-weight:700;font-size:18px;color:var(--blue);white-space:nowrap}
.brand-dot{width:26px;height:26px;border-radius:50%;background:var(--red)}
.nav{left:380px;top:27px;height:104px;display:flex;font-size:15px}
.nav a{color:#444;text-decoration:none;padding:0 9px;line-height:108px}
.nav a.active{background:var(--blue);color:#fff;padding:0 12px;position:relative}
.nav a.active::after{content:"";position:absolute;left:12px;right:12px;top:66px;height:2px;background:#fff}
.social{display:flex;gap:18px}
.social i{display:block;width:38px;height:38px;border-radius:50%;border:3px solid #8a9099;background:#fff}
.social i.blue{border-color:var(--blue)}
.social-top{left:850px;top:62px;gap:15px}

/* hero */
.counter{left:120px;top:249px;width:550px;height:260px;background:rgba(255,255,255,.92);text-align:center}
.counter .lead{margin-top:24px;font-size:30px;color:#222}
.counter .amount{font-family:"Roboto Condensed",sans-serif;font-weight:700;font-size:66px;color:var(--red);line-height:1.05;letter-spacing:1px}
.counter .tail{font-size:29px;color:#222}
.btn-red{display:inline-block;background:var(--red);color:#fff;border:3px solid #fff;box-shadow:0 0 0 1px #d9d9d9;font-size:25px;padding:4px 28px;margin-top:12px}
.dots{left:560px;top:648px;display:flex;gap:10px}
.dots i{width:11px;height:11px;background:#aab4c0;transform:rotate(45deg)}
.dots i.on{background:var(--blue)}

/* story */
.story-title{left:109px;top:1000px;font-family:"Roboto Condensed",sans-serif;font-weight:700;font-size:44px;line-height:50px;color:#fff}
.story{left:505px;top:716px;width:545px;color:#fff}
.story h3{font-family:"Roboto Condensed",sans-serif;font-size:22px;line-height:26px;margin-bottom:8px}
.story p{font-size:12px;line-height:25px;margin-bottom:25px}
.story p.right{text-align:right;padding-left:10px}

/* partners */
.section-head{width:1200px;left:0;text-align:center}
.partners-head h2{font-family:"Roboto Condensed",sans-serif;font-size:31px;color:#333;font-weight:700}
.partners-head p{font-size:13px;color:#666;margin-top:4px}
.partner-strip{left:0;top:1503px;width:1200px;height:109px;background:var(--pale)}
.badge{position:absolute;top:44px;width:66px;height:20px;border-radius:10px;background:#d2d6db}

/* search */
.search{left:114px;top:1680px}
.search h4{font-family:"Montserrat",sans-serif;font-size:16px;letter-spacing:2px;color:#333;font-weight:700}
.search p{font-size:13px;margin-top:14px;color:#333}
.search-form{left:114px;top:1757px;display:flex;height:46px}
.field{height:46px;background:#fff;border-right:1px solid #e3e3e3;font-size:13px;color:#888;padding:0 16px;line-height:46px}
.search-btn{width:187px;height:46px;background:var(--red);color:#fff;font-family:"Montserrat",sans-serif;font-weight:700;font-size:14px;letter-spacing:1px;text-align:center;line-height:46px}
.search-note{left:114px;top:1819px;font-size:12px;color:var(--red);display:flex;align-items:center;gap:8px}
.lock{width:12px;height:12px;background:var(--red);border-radius:2px}

/* features */
.features-head{left:69px;top:2040px}
.features-head h2{font-family:"Montserrat",sans-serif;font-size:38px;letter-spacing:5px;color:#fff;font-weight:700}
.features-head p{font-size:20px;letter-spacing:2px;color:var(--red);margin-top:2px}
.step{position:absolute;top:2220px;width:240px;margin-left:-120px;text-align:center;color:#fff}
.step-num{width:34px;height:34px;border-radius:50%;background:#fff;border:3px solid var(--blue-dark);color:var(--blue-dark);font-weight:700;font-size:13px;line-height:28px;margin:0 auto}
.step-stem{width:0;height:36px;border-left:2px dashed #fff;margin:6px auto 0}
.step-icon{width:150px;height:150px;border-radius:50%;background:var(--blue-dark);margin:17px auto 0;display:flex;align-items:center;justify-content:center}
.step h5{font-family:"Roboto Condensed",sans-serif;font-size:15px;font-weight:700;margin-top:20px}
.step p{font-size:13px;line-height:20px;width:170px;margin:0 auto}
.arrow{position:absolute;top:2362px;font-size:38px;color:#9cc2ea}

/* clients */
.clients-head h2{font-family:"Montserrat",sans-serif;font-weight:600;font-size:32px;color:#fff}
.clients-head p{font-size:13px;color:#bbb;margin-top:6px}
.diamond{position:absolute;width:12px;height:12px;background:var(--red);transform:rotate(45deg)}
.photo{position:absolute;border-radius:6px}
.quote{position:absolute;font-family:"Lora",serif;font-style:italic;font-size:16px;line-height:25px;color:#fff;white-space:nowrap}
.client-name{position:absolute;font-family:"Montserrat",sans-serif;color:var(--red)}
.client-name b{display:block;font-size:22px;font-weight:600}
.client-name small{display:block;font-size:12px;font-weight:700}

/* contact */
.contact-head h2{font-family:"Montserrat",sans-serif;font-weight:700;font-size:34px;letter-spacing:5px;color:#333}
.contact-head p{font-size:14px;color:#444;margin-top:2px}
.contact-box{left:122px;top:3342px;width:426px;height:413px;background:var(--blue);box-shadow:0 0 8px rgba(0,0,0,.25);text-align:center;color:#fff}
.contact-box h3{font-family:"Montserrat",sans-serif;font-size:30px;letter-spacing:4px;margin-top:30px}
.contact-box p{font-size:13px;margin-top:2px}
.input{position:absolute;left:26px;width:377px;height:50px;background:#fff;color:#aaa;font-size:13px;text-align:left;padding-left:14px;line-height:50px}
.send{position:absolute;left:26px;top:315px;width:377px;height:56px;background:var(--red);font-family:"Montserrat",sans-serif;font-weight:700;letter-spacing:2px;font-size:13px;line-height:56px}
.info{left:703px;top:3340px;font-size:13px;color:#666;line-height:25px}
.info h6{font-family:"Roboto Condensed",sans-serif;font-size:17px;font-weight:700;color:#222;margin:0 0 12px}
.info .block{margin-bottom:17px}
.social-contact{left:706px;top:3642px;gap:17px}
.to-top{left:1101px;top:3725px;width:33px;height:33px;background:var(--red);display:flex;align-items:center;justify-content:center}

/* footer */
.footer{left:0;top:3806px;width:1200px;height:211px;background:var(--darker);color:#ccc;font-size:11px}
.notch{position:absolute;left:590px;top:-10px;width:0;height:0;border-left:10px solid transparent;border-right:10px solid transparent;border-bottom:10px solid var(--darker)}
.copy{position:absolute;left:131px;top:47px;line-height:25px}
.copy em{color:var(--red);font-style:normal}
.subscribe{position:absolute;left:754px;top:46px;font-family:"Montserrat",sans-serif;font-weight:700;font-size:12px;color:#fff}
.subscribe-form{position:absolute;left:756px;top:84px;display:flex}
.subscribe-form span{width:213px;height:29px;border:1px solid #555;font-size:9px;color:#888;line-height:27px;padding-left:18px}
.subscribe-form b{width:87px;height:29px;background:var(--red);color:#fff;font-size:9px;text-align:center;line-height:29px}
.pay{position:absolute;top:175px;width:24px;height:14px;background:#666;border-radius:2px}
.foot-nav{position:absolute;left:756px;top:173px;font-size:11px;color:#ddd;display:flex}
.foot-nav a{color:#ddd;text-decoration:none;margin-right:28px}
</style>
</head>
<body>
<div class="page">

<svg class="backdrop" width="1200" height="4017" viewBox="0 0 1200 4017" aria-hidden="true">
  <defs>
    <linearGradient id="heroGrad" x1="0" y1="0" x2="1" y2="0.3">
      <stop offset="0" stop-color="#e8eef4"/>
      <stop offset="0.5" stop-color="#cfe1f2"/>
      <stop offset="1" stop-color="#3a9be8"/>
    </linearGradient>
    <linearGradient id="searchGrad" x1="0" y1="0" x2="1" y2="1">
      <stop offset="0" stop-color="#eef0f2"/>
      <stop offset="1" stop-color="#f8f8f8"/>
    </linearGradient>
  </defs>
  <rect x="0" y="131" width="1200" height="800" fill="url(#heroGrad)"/>
  <path d="M0,620 C200,600 360,715 560,700 C800,682 1010,630 1200,480 L1200,1410 C1000,1350 800,1318 600,1322 C380,1328 160,1440 0,1620 Z" fill="#1b5fa8"/>
  <rect x="0" y="1620" width="1200" height="400" fill="url(#searchGrad)"/>
  <path d="M0,1860 C250,1990 600,2030 1200,1900 L1200,3300 L0,3300 Z" fill="#3d3d3d"/>
  <path d="M0,2190 C300,2240 620,2170 880,2010 C1000,1950 1100,1930 1200,1925 L1200,2560 C1000,2640 700,2670 420,2665 C250,2662 100,2645 0,2625 Z" fill="#1b5fa8"/>
  <path d="M0,3250 C300,3170 650,3215 950,3160 C1060,3140 1140,3130 1200,3125 L1200,3806 L0,3806 Z" fill="#ffffff"/>
</svg>

<div class="abs topbar"><span>Call +001 555 0199</span><span>Email: info@brightwellrx.example</span></div>
<div class="abs header"></div>
<div class="abs brand"><span class="brand-dot"></span>Brightwell Rx Pass</div>
<nav class="abs nav">
  <a class="active" href="#">Home</a><a href="#">About us</a><a href="#">Partners</a><a href="#">Features</a><a href="#">Contact us</a>
</nav>
<div class="abs social social-top" aria-label="Social links"><i class="blue"></i><i></i><i></i><i></i></div>

<div class="abs" role="img" aria-label="Medical hexagon icons over a doctor holding a stethoscope" style="left:670px;top:131px;width:530px;height:360px;background:linear-gradient(135deg,rgba(47,139,224,.35),rgba(27,95,168,.6))"></div>

<div class="abs counter">
  <p class="lead">Till Date We have Saved Your</p>
  <p class="amount">$68,053,183.13</p>
  <p class="tail">From your medication bills</p>
  <span class="btn-red">Contact us..</span>
</div>
<div class="abs dots"><i></i><i class="on"></i><i></i><i></i></div>

<div class="abs" role="img" aria-label="Stack of discount cards" style="left:20px;top:560px;width:430px;height:270px;background:linear-gradient(135deg,#d9363a,#1e4f9c);transform:rotate(-28deg);border-radius:14px;opacity:.85"></div>

<h2 class="abs story-title">OUR<br>INTERESTING<br>STORY</h2>
<div class="abs story">
  <h3>Who We Are?</h3>
  <p>Photography is a powerful medium. It allows us to stay connected to the world and express ourselves creatively by sharing the content of our hearts without the need to communicate with words. Our creativity, emotions and feelings are captured through the images that we visualize in our minds and frame with our cameras.</p>
  <h3>Our Mission</h3>
  <p>Photography is a powerful medium. It allows us to stay connected to the world and express ourselves creatively by sharing the content of our hearts without the need to communicate with words. Our creativity, emotions and feelings are captured through the images that we visualize in our minds and frame with our cameras.</p>
  <h3>Our Focus</h3>
  <p>Photography is a powerful medium. It allows us to stay connected to the world and express ourselves creatively by sharing the content of our hearts without the need to communicate with words. Our creativity, emotions and feelings are captured through the images that we visualize in our minds and frame with our cameras.</p>
  <h3>Our History</h3>
  <p class="right">Photography is a powerful medium. It allows us to stay connected to the world and express ourselves creatively by sharing the content of our hearts without the need to communicate with words. Our creativity, emotions and feelings are captured through the images that we visualize in our minds and frame with our cameras.</p>
</div>

<div class="abs section-head partners-head" style="top:1393px"><h2>OUR PARTNERS</h2><p>Be a our partner to save on medication bills!</p></div>
<div class="abs partner-strip" aria-label="Partner badges">
  <i class="badge" style="left:120px"></i><i class="badge" style="left:300px;width:36px"></i><i class="badge" style="left:475px"></i><i class="badge" style="left:653px"></i><i class="badge" style="left:830px"></i><i class="badge" style="left:1008px"></i>
</div>

<div class="abs search"><h4>SEARCH A PHARMACY &amp; DRUG PRICE NOW?</h4><p>Enter your Drug Name, zip code and get price of drug along with location of pharmacy!</p></div>
<div class="abs search-form">
  <span class="field" style="width:182px">Drug Name</span>
  <span class="field" style="width:150px">ZIP CODE</span>
  <span class="field" style="width:188px">Within __ km</span>
  <span class="search-btn">Search Pharmacy</span>
</div>
<div class="abs search-note"><i class="lock"></i>* Enter the radious in kilometer in which you want to locate the pharmacy</div>

<div class="abs features-head"><h2>FEATURES</h2><p>SAVING YOUR MEDICATIONS</p></div>
<svg class="backdrop" width="1200" height="4017" aria-hidden="true"><line x1="250" y1="2238" x2="945" y2="2238" stroke="#fff" stroke-width="2" stroke-dasharray="14 8"/></svg>
<span class="arrow" style="left:70px">‹</span><span class="arrow" style="left:1100px">›</span>

<div class="step" style="left:229px">
  <div class="step-num">1</div><div class="step-stem"></div>
  <div class="step-icon"><svg width="96" height="96" viewBox="0 0 96 96"><polygon points="48,6 84,27 84,69 48,90 12,69 12,27" fill="#fff"/><rect x="36" y="34" width="24" height="28" rx="2" fill="none" stroke="#1b5fa8" stroke-width="3"/><line x1="41" y1="44" x2="55" y2="44" stroke="#1b5fa8" stroke-width="2"/><line x1="41" y1="51" x2="55" y2="51" stroke="#1b5fa8" stroke-width="2"/></svg></div>
  <h5>GET YOUR FREE CARD</h5><p>amet, consectetur adipisicing elit, sed do eiusmod tempor incididunt</p>
</div>
<div class="step" style="left:472px">
  <div class="step-num">2</div><div class="step-stem"></div>
  <div class="step-icon"><svg width="96" height="96" viewBox="0 0 96 96"><polygon points="48,6 84,27 84,69 48,90 12,69 12,27" fill="#fff"/><circle cx="39" cy="36" r="5" fill="#1b5fa8"/><circle cx="57" cy="36" r="5" fill="#1b5fa8"/><rect x="33" y="44" width="12" height="20" rx="3" fill="#1b5fa8"/><rect x="51" y="44" width="12" height="20" rx="3" fill="#1b5fa8"/></svg></div>
  <h5>HOW IT WORKS</h5><p>amet, consectetur adipisicing elit, sed do eiusmod tempor incididunt</p>
</div>
<div class="step" style="left:717px">
  <div class="step-num">3</div><div class="step-stem"></div>
  <div class="step-icon"><svg width="96" height="96" viewBox="0 0 96 96"><polygon points="48,6 84,27 84,69 48,90 12,69 12,27" fill="#fff"/><rect x="44" y="36" width="18" height="14" fill="#1b5fa8"/><circle cx="38" cy="42" r="4" fill="#1b5fa8"/><rect x="30" y="52" width="36" height="4" fill="#1b5fa8"/><rect x="34" y="48" width="8" height="14" fill="#1b5fa8"/></svg></div>
  <h5>CREATE YOUR CARD</h5><p>amet, consectetur adipisicing elit, sed do eiusmod tempor incididunt</p>
</div>
<div class="step" style="left:961px">
  <div class="step-num">4</div><div class="step-stem"></div>
  <div class="step-icon"><svg width="96" height="96" viewBox="0 0 96 96"><polygon points="48,6 84,27 84,69 48,90 12,69 12,27" fill="#fff"/><rect x="44" y="32" width="16" height="22" rx="2" fill="none" stroke="#1b5fa8" stroke-width="3"/><path d="M36 52 l8 4 v8 h-8 z" fill="#1b5fa8"/></svg></div>
  <h5>JOIN US</h5><p>amet, consectetur adipisicing elit, sed do eiusmod tempor incididunt</p>
</div>

<div class="abs section-head clients-head" style="top:2742px"><h2>Clients Says</h2><p>What our clients are saying about us?</p></div>
<i class="diamond" style="left:435px;top:2757px"></i><i class="diamond" style="left:738px;top:2757px"></i>
<div class="photo" role="img" aria-label="Smiling nurse in blue scrubs holding a folder" style="left:72px;top:2789px;width:222px;height:318px;background:linear-gradient(#4a9fd6,#2c7fb8)"></div>
<div class="photo" role="img" aria-label="Young man in a navy jacket wearing glasses" style="left:925px;top:2786px;width:181px;height:315px;background:linear-gradient(#3b4f7a,#23304f)"></div>
<p class="quote" style="left:301px;top:2918px">Sed ut perspiciatis<br>unde omnis iste natus error sit<br>voluptatem accusantium doloremque</p>
<p class="quote" style="left:600px;top:2918px;width:321px;text-align:right">Sed ut perspiciatis<br>unde omnis iste natus error sit<br>voluptatem accusantium doloremque</p>
<div class="client-name" style="left:300px;top:3040px"><b>Client Name</b><small>Bio-Tech Student</small></div>
<div class="client-name" style="left:700px;top:3038px;width:206px;text-align:right"><b>Client Name</b><small>University Professor</small></div>

<div class="abs section-head contact-head" style="top:3240px"><h2>CONTACT US</h2><p>if you have any query from us feel free to reach us</p></div>
<div class="abs contact-box">
  <h3>CONTACT US</h3><p>Contact us if you have any query from us</p>
  <span class="input" style="top:114px">Name</span>
  <span class="input" style="top:179px">Phone</span>
  <span class="input" style="top:246px">E-mail</span>
  <span class="send">SEND</span>
</div>
<div class="abs info">
  <div class="block"><h6>ADDRESS</h6>Building Number, Street Name. H.No. 23.<br>City name, State, Post Code.<br>Phone: +1-0123-456789</div>
  <div class="block"><h6>WEB</h6>website: www.Yourwebsite.com<br>Email: info@Yourwebsite.com</div>
  <h6>SOCIAL MEDIA</h6>
</div>
<div class="abs social social-contact" aria-label="Social links"><i class="blue"></i><i></i><i></i><i></i></div>
<div class="abs to-top"><svg width="14" height="10" viewBox="0 0 14 10"><path d="M1 9 L7 3 L13 9" fill="none" stroke="#fff" stroke-width="2.5"/></svg></div>

<footer class="abs footer">
  <span class="notch"></span>
  <div class="copy">Copyrights @ <em>Yourwebsite</em> 2015.<br>All rights reserved</div>
  <div class="subscribe">SUBSCRIBE <i style="font-family:Lora,serif">in</i> OUR NEWS LETTER</div>
  <div class="subscribe-form"><span>Enter Your Email Address</span><b>SUBSCRIBE</b></div>
  <i class="pay" style="left:134px"></i><i class="pay" style="left:177px"></i><i class="pay" style="left:212px"></i><i class="pay" style="left:250px"></i>
  <nav class="foot-nav"><a href="#">Home</a><a href="#">About us</a><a href="#">Terms &amp; Conditions</a><a href="#">Contact</a></nav>
</footer>

</div>
</body>
</html>
```